Northern Guild of Acute Care Doctors Membership Poster Design

We need a poster that highlights why physicians should become a member of our association.

As the national voice of emergency medicine (EM), NGAD provides continuing medical education, advocates on behalf of emergency physicians and their patients, supports research and strengthens the EM community. In co-operation with other specialties and committees, NGAD also plays a vital role in the development of national standards and clinical guidelines.

NGAD keeps Canadian emergency physicians informed of developments in the clinical practice of EM and addresses political and societal changes, that affect the delivery of emergency health care.

Vision
Leading excellence in Emergency Medicine across Canada

Mission
NGAD champions excellence in Emergency Medicine in Canada by:

Advocating for Emergency Physicians and their patients;
Connecting Emergency Physicians;
Leading Emergency Medicine education;
Fostering research and innovation
Defining standards for quality Emergency Care
Collaborating with Emergency Care providers.

Target Market(s)

Physicians, Residents and Medical Students

Industry/Entity Type

Doctor

Font styles to use
Sans Serif

Requirements
Must have
• Why belong?
• Career Development
• Vision
• Leading excellence in Emergency Medicine across Canada
• Mission
• NGAD champions excellence in Emergency Medicine in Canada by:
• Advocating for Emergency Physicians and their patients;
• Connecting Emergency Physicians;
• Leading Emergency Medicine education;
• Fostering research and innovation
• Defining standards for quality Emergency Care
• Collaborating with Emergency Care providers.
• Financial Discounts
• Special rates at Larchwood Inns
• Discount on fares from Trellis Lines
• Discounts on home and auto insurance thought the Hearthbond Mutual and Brightvale Cover
• Special rates on medical and dental insurance through Maplecrest Benefits
• Special rates with Pellam Mobile or Vexor
• Discounts on tickets from Dunholt Stageworks
• Discounts on tickets from Footlights on Tour
• Advocacy
• NGAD advocates on behalf of you and your patients
• We support the development of the specialty of emergency medicine for you
• Gain a larger voice representing you and your specialty
• Networking Opportunities
• Opportunity to become involved with NGAD committees and sections
• Connect with colleagues and potential mentors at events and through online discussions
• Member Types
• Physician Members
• Resident Members
• Student Members
• Associate Members
• ngad-example.ca
• Corporate colours or colours that are complimentary to our corporate colours
• Hex 0077b2
• Hex DF0631
Nice to have
• Pictures

```html
<!DOCTYPE html>
<html lang="en">
<head>
<meta charset="utf-8">
<title>NGAD Membership Poster</title>
<link rel="stylesheet" href="https://fonts.googleapis.com/css2?family=League+Spartan:wght@300;400;700;800&display=swap">
<style>
  :root {
    --paper: #ffffff;
    --photo-dark: #2c2622;
    --photo-mid: #5a514a;
    --photo-light: #8c8179;
    --headline: #f2f0ee;
    --body-text: #f4f2f0;
    --muted-text: #e2ddd8;
    --rule: rgba(244, 242, 240, 0.35);
    --brand-blue: #0077b2;
    --brand-red: #df0631;
  }
  * { margin: 0; padding: 0; box-sizing: border-box; }
  html, body {
    width: 789px;
    height: 1200px;
    overflow: hidden;
    background: var(--paper);
  }
  .poster {
    position: relative;
    width: 789px;
    height: 1200px;
    background: var(--paper);
    font-family: "League Spartan", "Helvetica Neue", Arial, sans-serif;
  }
  .hero-photo {
    position: absolute;
    left: 17px;
    top: 14px;
    width: 755px;
    height: 1174px;
    background:
      radial-gradient(ellipse 55% 40% at 50% 45%, var(--photo-light) 0%, rgba(140,129,121,0) 70%),
      radial-gradient(ellipse 60% 30% at 55% 88%, #7a6f67 0%, rgba(122,111,103,0) 70%),
      linear-gradient(160deg, var(--photo-dark) 0%, var(--photo-mid) 45%, #4a423c 100%);
  }
  .brand-mark {
    position: absolute;
    right: 40px;
    top: 40px;
    display: flex;
    align-items: center;
    gap: 10px;
  }
  .brand-mark__dot {
    width: 26px;
    height: 26px;
    border-radius: 50%;
    background: var(--brand-red);
  }
  .brand-mark__name {
    font-weight: 800;
    font-size: 40px;
    letter-spacing: 1px;
    color: var(--brand-blue);
    line-height: 1;
  }
  .headline {
    position: absolute;
    left: 17px;
    width: 755px;
    top: 222px;
    text-align: center;
    color: var(--headline);
    font-weight: 800;
    font-size: 88px;
    line-height: 79px;
    letter-spacing: -1px;
    text-transform: uppercase;
  }
  .copy {
    position: absolute;
    left: 124px;
    width: 541px;
    top: 814px;
    text-align: center;
    color: var(--body-text);
  }
  .copy__lead {
    font-weight: 700;
    font-size: 13.5px;
    margin-bottom: 10px;
  }
  .copy__para {
    font-weight: 300;
    font-size: 11.8px;
    line-height: 13.5px;
    margin-bottom: 11px;
  }
  .copy__call {
    font-weight: 700;
    font-size: 13.5px;
    margin-top: 2px;
  }
  .benefits {
    position: absolute;
    left: 42px;
    width: 705px;
    top: 966px;
    color: var(--muted-text);
    border-top: 1px solid var(--rule);
    padding-top: 6px;
  }
  .benefits__title {
    font-weight: 700;
    font-size: 12px;
    text-align: center;
    color: var(--body-text);
    margin-bottom: 4px;
  }
  .benefits__columns {
    column-count: 4;
    column-gap: 16px;
    font-size: 8.5px;
    line-height: 10px;
    font-weight: 400;
  }
  .benefit {
    margin-bottom: 4px;
  }
  .benefit__name {
    font-weight: 700;
    color: var(--body-text);
    break-after: avoid;
  }
  .benefit__list {
    list-style: none;
  }
  .benefit__list li {
    padding-left: 7px;
    text-indent: -7px;
  }
  .benefit__list li::before {
    content: "•";
    display: inline-block;
    width: 7px;
    text-indent: 0;
    color: var(--brand-red);
  }
  .site-address {
    position: absolute;
    left: 42px;
    top: 1150px;
    color: var(--body-text);
    font-weight: 700;
    font-size: 19px;
  }
</style>
</head>
<body>
  <main class="poster">
    <div class="hero-photo" role="img" aria-label="Close-up photograph of two gloved hands cupped protectively, one above the other, against a soft dark background"></div>

    <div class="brand-mark">
      <span class="brand-mark__dot"></span>
      <span class="brand-mark__name">NGAD</span>
    </div>

    <h1 class="headline">Be one<br>with<br>the past,<br>present and<br>future of<br>emergency<br>medicine.</h1>

    <section class="copy">
      <p class="copy__lead">Together, WE are the Northern Guild of Acute Care Doctors (NGAD)</p>
      <p class="copy__para">As the national voice of emergency medicine (EM), NGAD provides continuing medical education, advocates on behalf of emergency physicians and their patients, supports research and strengthens the EM community. In co-operation with other specialties and committees, NGAD also plays a vital role in the development of national standards and clinical guidelines.</p>
      <p class="copy__para">NGAD keeps Canadian emergency physicians informed of developments in the clinical practice of EM and addresses political and societal changes, that affect the delivery of emergency health care.</p>
      <p class="copy__call">It’s always reassuring to know we’re in good hands. Join NGAD today.</p>
    </section>

    <section class="benefits">
      <h2 class="benefits__title">Why belong?</h2>
      <div class="benefits__columns">
        <div class="benefit">
          <p class="benefit__name">Career Development</p>
        </div>
        <div class="benefit">
          <p class="benefit__name">Vision</p>
          <p>Leading excellence in Emergency Medicine across Canada</p>
        </div>
        <div class="benefit">
          <p class="benefit__name">Mission</p>
          <p>NGAD champions excellence in Emergency Medicine in Canada by:</p>
          <ul class="benefit__list">
            <li>Advocating for Emergency Physicians and their patients;</li>
            <li>Connecting Emergency Physicians;</li>
            <li>Leading Emergency Medicine education;</li>
            <li>Fostering research and innovation</li>
            <li>Defining standards for quality Emergency Care</li>
            <li>Collaborating with Emergency Care providers.</li>
          </ul>
        </div>
        <div class="benefit">
          <p class="benefit__name">Financial Discounts</p>
          <ul class="benefit__list">
            <li>Special rates at Larchwood Inns</li>
            <li>Discount on fares from Trellis Lines</li>
            <li>Discounts on home and auto insurance thought the Hearthbond Mutual and Brightvale Cover</li>
            <li>Special rates on medical and dental insurance through Maplecrest Benefits</li>
            <li>Special rates with Pellam Mobile or Vexor</li>
            <li>Discounts on tickets from Dunholt Stageworks</li>
            <li>Discounts on tickets from Footlights on Tour</li>
          </ul>
        </div>
        <div class="benefit">
          <p class="benefit__name">Advocacy</p>
          <ul class="benefit__list">
            <li>NGAD advocates on behalf of you and your patients</li>
            <li>We support the development of the specialty of emergency medicine for you</li>
            <li>Gain a larger voice representing you and your specialty</li>
          </ul>
        </div>
        <div class="benefit">
          <p class="benefit__name">Networking Opportunities</p>
          <ul class="benefit__list">
            <li>Opportunity to become involved with NGAD committees and sections</li>
            <li>Connect with colleagues and potential mentors at events and through online discussions</li>
          </ul>
        </div>
        <div class="benefit">
          <p class="benefit__name">Member Types</p>
          <ul class="benefit__list">
            <li>Physician Members</li>
            <li>Resident Members</li>
            <li>Student Members</li>
            <li>Associate Members</li>
          </ul>
        </div>
      </div>
    </section>

    <p class="site-address">ngad-example.ca</p>
  </main>
</body>
</html>
```